Investigation Before Elimination

Create a very professional and eye-catching Infographic for Birchline Supply that is intended to convey to retailers that they should investigate why products are NOT selling in the Birchline Supply store before they apply a discount to get rid of it. The infographic should capture all of the questions they should think about before making cutting the price. See the attachment for details on wording.

Target Market(s)

Birchline Supply Business Owners

Industry/Entity Type

Retail

Font styles to use
Sans Serif

Requirements
Must have
• Any product in the infographic must be home improvement related product. See our website for ideas:
https://www.birchlinesupply.example/?utm_source=google&utm_medium=cpc&gclid=QwpLMnRt8X4ZkHFpTvB3YcNE7q_rs2JkWbhv8mYd204_7Gf-xlPQe4pm88sRyTzGk2Vq6-Lbh-yXpLW-mdNwBnq_CvA&gclsrc=aw.ds

* Must be in Birchline Supply related colors
* Must be fun, exciting, eye-catching, unique, and clever
* 1-Page preferable but no more than two standard 8-1/2"x11"
* See the attachment for details on wording.
Should not have
• N/A

```html
<!DOCTYPE html>
<html lang="en">
<head>
<meta charset="utf-8">
<title>Investigation Before Elimination — Birchline Supply</title>
<link rel="stylesheet" href="https://fonts.googleapis.com/css2?family=Roboto+Slab:wght@700;800&family=Roboto:wght@400;500;700&display=swap">
<style>
  :root{
    --ink:#3b3b3b;
    --brand-red:#e31d3a;
    --deep-red:#b31f28;
    --blue:#5256a6;
    --green:#7dbf45;
    --sky:#6db7e2;
    --purple:#9b5e9f;
    --orange:#e8892c;
    --charcoal:#3a3a3a;
    --teal:#26b39d;
    --footer-bg:#e4e4e4;
    --bar-bg:#8a8482;
    --bar-dark:#4d4d4d;
    --white:#ffffff;
  }
  *{margin:0;padding:0;box-sizing:border-box}
  html,body{width:927px;height:1200px;overflow:hidden;background:var(--white)}
  body{font-family:"Roboto",Arial,sans-serif;color:var(--ink)}
  .sheet{position:relative;width:927px;height:1200px;overflow:hidden}
  .funnel-art{position:absolute;left:0;top:0}
  .headline{position:absolute;left:55px;top:60px;font-family:"Roboto Slab",Georgia,serif;font-weight:800;letter-spacing:-1px;white-space:nowrap}
  .headline-top{display:block;margin-left:45px;font-size:56px;line-height:62px;color:var(--ink)}
  .headline-bottom{display:flex;align-items:center;gap:8px;margin-top:0}
  .before-tag{background:var(--ink);color:var(--white);font-family:"Roboto",Arial,sans-serif;font-weight:400;font-size:27px;letter-spacing:1px;padding:2px 10px 1px;line-height:32px}
  .headline-red{font-size:56px;line-height:62px;color:var(--brand-red)}
  .brand-mark{position:absolute;left:670px;top:80px;width:205px;display:flex;align-items:center;gap:12px}
  .brand-square{width:28px;height:28px;background:var(--brand-red);flex:none}
  .brand-name{font-family:"Roboto",Arial,sans-serif;font-weight:700;font-size:30px;line-height:32px;color:var(--brand-red)}
  .rule{position:absolute;left:55px;top:181px;width:817px;border-top:2px dotted #8c8c8c}
  .lead{position:absolute;left:76px;top:199px;width:775px;text-align:center;font-weight:700;font-size:20px;line-height:25px;color:var(--ink)}
  .sublead{position:absolute;left:64px;top:305px;width:799px;text-align:center;font-size:14.5px;line-height:21px;color:var(--ink)}
  .step{position:absolute;width:540px}
  .step-q{font-weight:700;font-size:13.5px;line-height:17px}
  .step-a{font-size:11.5px;line-height:14px;color:var(--ink);margin-top:2px}
  .s1 .step-q{color:var(--deep-red)} .s2 .step-q{color:var(--blue)} .s3 .step-q{color:var(--green)}
  .s4 .step-q{color:var(--sky)} .s5 .step-q{color:var(--purple)} .s6 .step-q{color:var(--orange)}
  .s7 .step-q{color:var(--charcoal)} .s8 .step-q{color:var(--teal)}
  .final-step{position:absolute;left:290px;top:945px;font-size:19px;color:var(--brand-red)}
  .final-step .chip{background:var(--brand-red);color:var(--white);font-weight:700;padding:0 4px}
  .resources{position:absolute;left:0;top:1014px;width:927px;height:104px;background:var(--footer-bg);text-align:center;padding-top:21px;font-size:16px;line-height:21px;color:var(--ink);white-space:nowrap}
  .resource-links{color:var(--brand-red)}
  .resource-links .sep{color:var(--ink);margin:0 6px}
  .contact-bar{position:absolute;left:0;top:1118px;width:927px;height:82px;background:var(--bar-bg);color:var(--white);font-size:14px;display:flex;align-items:center;padding-left:62px;gap:8px;white-space:nowrap}
  .contact-bar::before{content:"";position:absolute;left:0;top:0;width:22px;height:82px;background:var(--bar-dark)}
  .contact-bar::after{content:"";position:absolute;left:22px;top:0;width:20px;height:82px;background:var(--brand-red)}
  .contact-item{display:flex;align-items:center;gap:6px;margin-left:6px}
</style>
</head>
<body>
<main class="sheet">
  <svg class="funnel-art" width="927" height="1000" viewBox="0 0 927 1000" aria-hidden="true">
    <defs>
      <linearGradient id="row1" x1="0" x2="1"><stop offset="0" stop-color="#f6d3d4"/><stop offset="1" stop-color="#fff" stop-opacity="0"/></linearGradient>
      <linearGradient id="row2" x1="0" x2="1"><stop offset="0" stop-color="#d9daee"/><stop offset="1" stop-color="#fff" stop-opacity="0"/></linearGradient>
      <linearGradient id="row3" x1="0" x2="1"><stop offset="0" stop-color="#e2f0d3"/><stop offset="1" stop-color="#fff" stop-opacity="0"/></linearGradient>
      <linearGradient id="row4" x1="0" x2="1"><stop offset="0" stop-color="#d8ecf8"/><stop offset="1" stop-color="#fff" stop-opacity="0"/></linearGradient>
      <linearGradient id="row5" x1="0" x2="1"><stop offset="0" stop-color="#eadcec"/><stop offset="1" stop-color="#fff" stop-opacity="0"/></linearGradient>
      <linearGradient id="row6" x1="0" x2="1"><stop offset="0" stop-color="#fbe2c9"/><stop offset="1" stop-color="#fff" stop-opacity="0"/></linearGradient>
      <linearGradient id="row7" x1="0" x2="1"><stop offset="0" stop-color="#dedede"/><stop offset="1" stop-color="#fff" stop-opacity="0"/></linearGradient>
      <linearGradient id="row8" x1="0" x2="1"><stop offset="0" stop-color="#d2efe9"/><stop offset="1" stop-color="#fff" stop-opacity="0"/></linearGradient>
      <linearGradient id="row9" x1="0" x2="1"><stop offset="0" stop-color="#fcd6da"/><stop offset="1" stop-color="#fff" stop-opacity="0"/></linearGradient>
      <marker id="arrowhead" markerWidth="10" markerHeight="10" refX="5" refY="5" orient="auto"><path d="M0,0 L10,5 L0,10 z" fill="#e31d3a"/></marker>
    </defs>

    <polygon points="410,434 870,434 870,495 394,495" fill="url(#row1)"/>
    <polygon points="394,495 870,495 870,557 379,557" fill="url(#row2)"/>
    <polygon points="379,557 870,557 870,618 363,618" fill="url(#row3)"/>
    <polygon points="363,618 870,618 870,680 347,680" fill="url(#row4)"/>
    <polygon points="347,680 870,680 870,742 332,742" fill="url(#row5)"/>
    <polygon points="332,742 870,742 870,803 316,803" fill="url(#row6)"/>
    <polygon points="316,803 870,803 870,865 300,865" fill="url(#row7)"/>
    <polygon points="300,865 870,865 870,927 284,927" fill="url(#row8)"/>
    <polygon points="284,927 870,927 870,987 254,987" fill="url(#row9)"/>

    <g>
      <polygon points="388,372 410,434 394,495 372,433" fill="#d57f72"/>
      <polygon points="372,433 394,495 379,557 357,495" fill="#9d9fd0"/>
      <polygon points="357,495 379,557 363,618 341,556" fill="#b5dc90"/>
      <polygon points="341,556 363,618 347,680 325,618" fill="#b2dbf2"/>
      <polygon points="325,618 347,680 332,742 310,680" fill="#c8a6cb"/>
      <polygon points="310,680 332,742 316,803 294,741" fill="#f3bd8a"/>
      <polygon points="294,741 316,803 300,865 278,803" fill="#8d8d8d"/>
      <polygon points="278,803 300,865 284,927 263,865" fill="#96dccf"/>
      <polygon points="263,865 284,927 254,987 247,925" fill="#f2a9ae"/>
      <polygon points="247,925 254,987 244,987 232,985" fill="#f2b6a8"/>
    </g>
    <g fill="#fff" font-family="Roboto, Arial, sans-serif" font-weight="700" font-size="22">
      <text transform="translate(384,418) rotate(72)" text-anchor="middle">01</text>
      <text transform="translate(368,480) rotate(72)" text-anchor="middle">02</text>
      <text transform="translate(353,541) rotate(72)" text-anchor="middle">03</text>
      <text transform="translate(337,603) rotate(72)" text-anchor="middle">04</text>
      <text transform="translate(321,665) rotate(72)" text-anchor="middle">05</text>
      <text transform="translate(306,726) rotate(72)" text-anchor="middle">06</text>
      <text transform="translate(290,788) rotate(72)" text-anchor="middle">07</text>
      <text transform="translate(275,850) rotate(72)" text-anchor="middle">08</text>
    </g>

    <polygon points="55,372 388,372 372.5,433 72.6,433" fill="#b31f28"/>
    <polygon points="72.6,433 372.5,433 356.7,495 90.5,495" fill="#5256a6"/>
    <polygon points="90.5,495 356.7,495 341.2,556 108.2,556" fill="#7dbf45"/>
    <polygon points="108.2,556 341.2,556 325.4,618 126.1,618" fill="#6db7e2"/>
    <polygon points="126.1,618 325.4,618 309.6,680 144,680" fill="#9b5e9f"/>
    <polygon points="144,680 309.6,680 294.1,741 161.6,741" fill="#e8892c"/>
    <polygon points="161.6,741 294.1,741 278.3,803 179.6,803" fill="#3a3a3a"/>
    <polygon points="179.6,803 278.3,803 262.5,865 197.5,865" fill="#26b39d"/>
    <polygon points="197.5,865 262.5,865 247.3,925 214.8,925" fill="#e31d3a"/>
    <polygon points="214.8,925 247.3,925 232,985" fill="#ef8a80"/>

    <g fill="none" stroke="#fff" stroke-width="2.2" stroke-linejoin="round" stroke-linecap="round">
      <g transform="translate(221,402)">
        <path d="M-16,-6 L0,-14 L16,-6 L0,2 Z M-16,-6 L-16,12 L0,20 L16,12 L16,-6 M0,2 L0,20 M-16,-6 L-21,1 L-5,9 L0,2 M16,-6 L21,1 L5,9 L0,2"/>
      </g>
      <g transform="translate(222,464)">
        <path d="M-20,-16 L-20,20 M20,-16 L20,20 M-20,-4 L20,-4 M-20,8 L20,8 M-20,20 L20,20"/>
        <path d="M-15,-4 v-10 h5 v10 M-6,-4 v-10 h5 v10 M3,-4 v-10 h5 v10 M12,-4 v-10 h4 v10 M-15,8 v-8 h8 v8 M-3,8 v-8 h8 v8 M9,8 v-8 h7 v8 M-15,20 v-8 h8 v8 M-3,20 v-8 h8 v8 M9,20 v-8 h7 v8"/>
      </g>
      <g transform="translate(224,525) rotate(-35)">
        <path d="M-20,-10 L10,-10 L20,0 L10,10 L-20,10 Z"/>
        <circle cx="10" cy="0" r="2.5"/>
        <text x="-9" y="6" fill="#fff" stroke="none" font-family="Roboto, Arial, sans-serif" font-weight="700" font-size="16" text-anchor="middle">$</text>
      </g>
      <g transform="translate(225,587)">
        <path d="M-16,0 L16,0 L16,18 L-16,18 Z M-16,0 L-21,-6 M16,0 L21,-6"/>
        <circle cx="0" cy="-10" r="6"/>
        <path d="M-3,-3 h6 M0,-22 v-4 M-11,-14 l-3,-2 M11,-14 l3,-2"/>
      </g>
      <g transform="translate(225,649)">
        <path d="M-20,-12 v-6 h6 M14,-18 h6 v6 M-20,12 v6 h6 M20,12 v6 h-6"/>
        <circle cx="2" cy="2" r="7"/>
        <path d="M7,7 L13,13"/>
      </g>
      <g transform="translate(227,710)">
        <path d="M-22,-14 h6 l6,22 h22 l5,-16 h-30"/>
        <circle cx="-6" cy="15" r="3"/><circle cx="9" cy="15" r="3"/>
      </g>
      <g transform="translate(228,772)">
        <path d="M-18,-2 h36 l-4,18 h-28 Z M-12,-2 q12,-20 24,0 M-8,4 v8 M0,4 v8 M8,4 v8"/>
      </g>
      <g transform="translate(229,834) rotate(-15)">
        <path d="M-13,-20 h26 v36 l-13,6 l-13,-6 Z"/>
        <rect x="-10" y="-6" width="20" height="8" fill="#fff" stroke="none"/>
        <path d="M-8,8 h16 M-8,13 h16 M0,-20 v-6"/>
      </g>
      <g transform="translate(230,893)">
        <circle r="10"/>
        <path d="M-5,0 l3.5,4 l6,-7"/>
      </g>
    </g>

    <line x1="47" y1="382" x2="190" y2="880" stroke="#e31d3a" stroke-width="2" marker-end="url(#arrowhead)"/>
    <path d="M243,947 L243,957 L280,957" fill="none" stroke="#fff" stroke-width="1.6" stroke-dasharray="2 3"/>
    <path d="M279,953 l5,4 l-5,4" fill="#fff"/>
  </svg>

  <header>
    <h1 class="headline">
      <span class="headline-top">INVESTIGATION</span>
      <span class="headline-bottom"><span class="before-tag">BEFORE</span><span class="headline-red">ELIMINATION</span></span>
    </h1>
    <div class="brand-mark"><span class="brand-square"></span><span class="brand-name">Birchline Supply</span></div>
  </header>

  <div class="rule"></div>

  <p class="lead">Dead stock in your store rapidly eats away at profits, drives up the cost of doing business, and occupies valuable shelf space that would be better served by fresh and more productive products. To address this issue, a typical knee-jerk response is marking down the product and attempting to sell it at a discount.</p>
  <p class="sublead">Though this is a better approach than simply hoping it sells ‘one day’, applying a markdown should be used only as a last resort after sales floor investigation takes place for common execution issues that are known to hamper sales;</p>

  <section class="steps">
    <div class="step s1" style="left:420px;top:443px">
      <p class="step-q">Is the product physically there?</p>
      <p class="step-a">One of the most typical issues is that the item is no longer existent<br>(i.e. ghost inventory)</p>
    </div>
    <div class="step s2" style="left:405px;top:511px">
      <p class="step-q">Is the item merchandised properly - Is it in plain view of the customer?</p>
      <p class="step-a">Find out if it is stuck in the backroom, top stock, or buried behind other products</p>
    </div>
    <div class="step s3" style="left:389px;top:566px">
      <p class="step-q">Is the item priced competitively?</p>
      <p class="step-a">In today’s price sensitive market, making sure the cost of the SKU is in line with<br>the customer expectation is key</p>
    </div>
    <div class="step s4" style="left:373px;top:634px">
      <p class="step-q">Is the physical product and packaging in a desirable condition?</p>
      <p class="step-a">Bottom-line: Nobody wants ripped or torn, or physically abused merchandise</p>
    </div>
    <div class="step s5" style="left:352px;top:685px">
      <p class="step-q">Is the sale of the SKU independent of the sale of another item?</p>
      <p class="step-a">With SKUs that depend on each other to sell, analyze the sell through and<br>performance of the other item</p>
    </div>
    <div class="step s6" style="left:335px;top:750px">
      <p class="step-q">Is the stock for the item enough for the customer to want to make the purchase?</p>
      <p class="step-a">Seldom do consumers come in to buy one or two casters (i.e. project SKU). Having sufficient<br>quantity to sell the job quantity is key</p>
    </div>
    <div class="step s7" style="left:318px;top:820px">
      <p class="step-q">Is the item still relevant to the shopper?</p>
      <p class="step-a">Get rid of outdated product and technology… those old rotary dial phone cords!</p>
    </div>
    <div class="step s8" style="left:298px;top:880px">
      <p class="step-q">Is the item unique enough to where an alike SKU &nbsp;isn’t cannibalizing its sales?</p>
      <p class="step-a">Each SKU needs to be different and stand on its own. Eliminate redundancies in the product mix</p>
    </div>
    <p class="final-step">Implement <span class="chip">Markdown</span> Strategy</p>
  </section>

  <footer>
    <div class="resources">
      <p>For further detail on in-stock position, see the following resources:</p>
      <p class="resource-links">Obsolete Inventory - Closeout Management (COM) Setup<span class="sep">|</span>In-Stock Procedures<span class="sep">|</span>Markdown Strategy</p>
      <p>Visit: https://birchnet.birchlineservices.example/bwor/inventory-management</p>
    </div>
    <div class="contact-bar">
      <span>For more information, contact Store Systems and Operations:</span>
      <span class="contact-item">
        <svg width="22" height="22" viewBox="0 0 24 24" aria-hidden="true"><circle cx="12" cy="12" r="10.5" fill="none" stroke="#fff" stroke-width="1.6"/><path d="M8.5,6.5 l2,2.5 -1.2,1.5 c0.8,1.8 2.2,3.2 4,4 l1.5,-1.2 2.5,2 -1.3,1.8 c-4,-0.5 -8,-4.5 -8.5,-8.5 z" fill="#fff"/></svg>
        555.014.2290
      </span>
      <span class="contact-item">
        <svg width="26" height="18" viewBox="0 0 26 18" aria-hidden="true"><rect x="1" y="1" width="24" height="16" fill="none" stroke="#fff" stroke-width="1.6"/><path d="M1,1 L13,10 L25,1 M1,17 L10,8 M25,17 L16,8" fill="none" stroke="#fff" stroke-width="1.6"/></svg>
        storeoperations@birchlinesupply.example
      </span>
    </div>
  </footer>
</main>
</body>
</html>
```